Accounting and Financial Services Firm - Modern, Fresh, Original, Professional

We need a business card designed. We would like to see use of the the colors blue. Logo attached.

Modern, Fresh, Original, Professional,
Updates

Email section on business card required. design brief updated.

Target Market(s)

Small to medium businesses and high net worth individuals

Industry/Entity Type

Public Accounting

Contact Information for Business Card

Business Name: PM Ledgerline Chartered Accountants
Address: Level 14, 82 Harrow Lane Sydney NSW 2000
Ph: 02 9314 2587
Mobile: 04 XXXX XXXX
Email: anna@pmledgerline.com.au
Chat ID: XXXXXXX
Website: www.pmledgerline.com.au

Name: Anna Petrov
Position: Manager

Font styles to use
Sans Serif

Colors
0492cd
33a6d7
85cae6

Requirements
Must have
• Modern font.

```html
<!DOCTYPE html>
<html lang="en">
<head>
<meta charset="utf-8">
<title>PM Ledgerline Business Card</title>
<link rel="stylesheet" href="https://fonts.googleapis.com/css2?family=Roboto:ital,wght@0,400;0,500;0,700;1,400;1,700&display=swap">
<style>
  :root {
    --blue: #0492cd;
    --blue-mid: #33a6d7;
    --blue-light: #85cae6;
    --blue-deep: #0a5fb4;
    --paper: #f1f1f0;
    --ink: #2a2a2a;
    --grey: #9a9a9a;
    --rule: #b8b8b8;
    --backdrop: #1e1e20;
    --chat: #3aa53a;
  }
  * { margin: 0; padding: 0; box-sizing: border-box; }
  html, body { width: 1200px; height: 1053px; overflow: hidden; }
  body {
    background: var(--backdrop);
    font-family: "Roboto", Arial, sans-serif;
    position: relative;
  }
  .card {
    position: absolute;
    left: 220px;
    width: 760px;
    height: 464px;
    border-radius: 4px;
    overflow: hidden;
  }
  /* Front */
  .card-front { top: 40px; background: var(--paper); }
  .person { position: absolute; left: 56px; top: 92px; }
  .person-name {
    font-weight: 700; font-size: 40px; color: var(--blue); letter-spacing: -0.3px;
  }
  .person-role { font-size: 21px; color: var(--ink); margin-top: 4px; }
  .divider {
    position: absolute; left: 56px; right: 56px; top: 222px;
    height: 1px; background: var(--rule);
  }
  .contacts { position: absolute; left: 56px; top: 246px; list-style: none; }
  .contacts li {
    display: flex; align-items: center; gap: 16px;
    font-size: 21px; color: var(--ink); line-height: 38px;
  }
  .contacts svg { width: 20px; height: 20px; flex: none; }
  .brand {
    position: absolute; right: 56px; top: 128px;
    display: flex; align-items: center; gap: 14px;
  }
  .brand-mark { width: 26px; height: 26px; background: var(--blue); }
  .brand-name {
    font-weight: 500; font-size: 24px; color: var(--blue);
    line-height: 1.25; text-transform: uppercase; letter-spacing: 1.5px;
  }
  .office { position: absolute; right: 56px; top: 250px; text-align: left; }
  .chat-id {
    display: flex; align-items: center; gap: 10px;
    font-size: 21px; color: var(--ink); line-height: 36px;
  }
  .chat-id .label { color: var(--chat); font-weight: 700; font-style: italic; }
  .chat-dot { width: 16px; height: 16px; border-radius: 50%; background: var(--chat); }
  .address { font-size: 21px; color: var(--ink); line-height: 32px; }
  .front-band {
    position: absolute; left: 0; bottom: 0; width: 100%; height: 16px;
    background: var(--blue);
  }
  .band-chips {
    position: absolute; right: 0; bottom: 0; display: flex; height: 16px;
  }
  .band-chips span { width: 26px; height: 16px; }
  .chip-light { background: var(--blue-light); }
  .chip-pale { background: #d8d8d8; }
  .chip-grey { background: var(--grey); }
  /* Back */
  .card-back {
    top: 549px;
    background: linear-gradient(160deg, var(--blue-mid) 0%, var(--blue) 45%, var(--blue-deep) 100%);
    display: flex; flex-direction: column; align-items: center; justify-content: center;
    color: #fff;
  }
  .back-brand { display: flex; align-items: center; gap: 18px; }
  .back-brand .brand-mark { width: 34px; height: 34px; background: #e8e8e8; }
  .back-brand .brand-name { color: #fff; font-size: 32px; letter-spacing: 2px; }
  .website { margin-top: 34px; font-size: 22px; font-weight: 500; color: #e6f3fa; }
</style>
</head>
<body>
  <section class="card card-front" aria-label="Business card front">
    <div class="person">
      <div class="person-name">Anna Petrov</div>
      <div class="person-role">Manager</div>
    </div>
    <div class="divider"></div>
    <ul class="contacts">
      <li>
        <svg viewBox="0 0 20 20" aria-hidden="true"><path d="M5 2 L8 2 L9 6 L7 8 Q9 12 12 13 L14 11 L18 12 L18 15 Q17 18 14 18 Q4 16 2 5 Q2 2 5 2 Z" fill="var(--blue)"/></svg>
        02 9314 2587
      </li>
      <li>
        <svg viewBox="0 0 20 20" aria-hidden="true"><rect x="5" y="1.5" width="10" height="17" rx="2" fill="none" stroke="var(--blue-mid)" stroke-width="1.6"/><circle cx="10" cy="15.5" r="1" fill="var(--blue-mid)"/></svg>
        04 XXXX XXXX
      </li>
      <li>
        <svg viewBox="0 0 20 20" aria-hidden="true"><rect x="1.5" y="4" width="17" height="12" fill="none" stroke="var(--grey)" stroke-width="1.5"/><path d="M1.5 4 L10 11 L18.5 4" fill="none" stroke="var(--grey)" stroke-width="1.5"/></svg>
        anna@pmledgerline.com.au
      </li>
    </ul>
    <div class="brand">
      <span class="brand-mark"></span>
      <div class="brand-name">PM Ledgerline<br>Chartered Accountants</div>
    </div>
    <div class="office">
      <div class="chat-id"><span class="chat-dot"></span><span class="label">Chat ID :</span> XXXXXXX</div>
      <div class="address">Level 14, 82 Harrow Lane<br>Sydney NSW 2000</div>
    </div>
    <div class="front-band"></div>
    <div class="band-chips"><span class="chip-light"></span><span class="chip-pale"></span><span class="chip-grey"></span></div>
  </section>

  <section class="card card-back" aria-label="Business card back">
    <div class="back-brand">
      <span class="brand-mark"></span>
      <div class="brand-name">PM Ledgerline<br>Chartered Accountants</div>
    </div>
    <div class="website">www.pmledgerline.com.au</div>
  </section>
</body>
</html>
```